Property Developer - Simple yet Sophisticated and Sharp Business Card

We are a medium sized property developer involved mainly in townhouse developments and land subdivisions.

The company is looking for a simple, sharp and sophisticated business card that will be given to contractors, land owners, financiers etc and thus will need to look professional.

Property development related graphics and art can be used, however the card is not to be too "busy" or crowded. Our company name is KL Estates which could possibly be incorporated into the graphics or artwork.

Single sided and/or double sided designs will be acceptable.

A Simple, Sophisticated, Sharp design please!

Good Luck !

```html
<!DOCTYPE html>
<html lang="en">
<head>
<meta charset="utf-8">
<title>KL Estates – Business Card Concepts</title>
<link rel="stylesheet" href="https://fonts.googleapis.com/css2?family=Open+Sans:wght@300;400;600;700;800&display=swap">
<style>
  :root{
    --brand-blue:#0b93c9;
    --brand-blue-deep:#0780b3;
    --brand-blue-light:#1aa3d6;
    --charcoal:#464749;
    --text-grey:#4d4d4f;
    --paper:#ffffff;
    --canvas:#ffffff;
  }
  *{margin:0;padding:0;box-sizing:border-box}
  html,body{width:1200px;height:689px;overflow:hidden;background:var(--canvas)}
  body{position:relative;font-family:"Open Sans",Arial,sans-serif}

  .card{position:absolute;width:584px;height:330px;overflow:hidden}
  .card--front{left:13px;background:var(--paper)}
  .card--back{left:605px;background:linear-gradient(180deg,var(--brand-blue-light) 0%,var(--brand-blue) 50%,var(--brand-blue-deep) 100%)}
  .row-1{top:9px}
  .row-2{top:353px}

  /* wordmark */
  .wordmark{position:absolute;display:flex;align-items:center;gap:12px}
  .wordmark__dot{border-radius:50%;flex:none}
  .wordmark__name{font-weight:800;letter-spacing:0.5px;line-height:1;white-space:nowrap}
  .card--front .wordmark{left:42px;top:34px}
  .card--front .wordmark__dot{width:60px;height:60px;background:var(--brand-blue)}
  .card--front .wordmark__name{font-size:26px;color:var(--charcoal)}
  .card--back .wordmark{left:50%;top:50%;transform:translate(-50%,-50%)}
  .card--back .wordmark__dot{width:84px;height:84px;background:var(--paper)}
  .card--back .wordmark__name{font-size:34px;color:var(--paper)}

  .back-ring{position:absolute;left:-40px;top:-90px;width:520px;height:520px;border-radius:50%;background:rgba(255,255,255,0.07)}

  /* identity */
  .person{position:absolute;left:0;top:170px;width:230px;height:50px}
  .person__name{position:absolute;left:36px;top:0;font-size:27px;font-weight:300;color:var(--brand-blue);letter-spacing:-0.5px;line-height:1}
  .person__bar{position:absolute;left:0;top:30px}
  .person__role{position:absolute;left:104px;top:30px;font-size:8.5px;font-weight:600;color:var(--paper);letter-spacing:0.3px;line-height:10px}

  .divider{position:absolute;left:248px;top:172px;width:1px;height:70px;background:var(--brand-blue)}

  .contacts{position:absolute;left:266px;top:172px;list-style:none}
  .contacts li{display:flex;align-items:center;gap:9px;height:19px;font-size:11.5px;color:var(--text-grey);text-transform:uppercase;letter-spacing:0.2px}
  .contacts svg{width:14px;height:12px;flex:none}

  .footer-band{position:absolute;left:0;right:0;top:291px;height:25px;background:var(--charcoal)}
  .footer-band svg{position:absolute;left:428px;top:0}
  .footer-stripe{position:absolute;left:0;right:0;top:316px;height:14px;background:var(--brand-blue)}
</style>
</head>
<body>

<!-- Concept A & B fronts share a layout -->
<section class="card card--front row-1">
  <div class="wordmark"><span class="wordmark__dot"></span><span class="wordmark__name">KL ESTATES</span></div>
  <div class="person">
    <p class="person__name">DANIEL HART</p>
    <svg class="person__bar" width="220" height="11" viewBox="0 0 220 11"><polygon points="0,2 88,2 92,5.5 88,9 0,9" fill="#464749"/><polygon points="92,0 212,0 218,5.5 212,11 92,11 97,5.5" fill="#464749"/></svg>
    <p class="person__role">GENERAL MANAGER</p>
  </div>
  <div class="divider"></div>
  <ul class="contacts">
    <li><svg viewBox="0 0 14 12"><rect x="1" y="1" width="12" height="7" fill="none" stroke="#4d4d4f" stroke-width="1.5"/><rect x="0" y="9" width="14" height="2.5" fill="#4d4d4f"/></svg>+ (07) 3250 6184</li>
    <li><svg viewBox="0 0 14 12"><rect x="3" y="0" width="8" height="4" fill="#4d4d4f"/><rect x="0" y="4" width="14" height="5" rx="1" fill="#4d4d4f"/><rect x="3" y="8" width="8" height="4" fill="#fff" stroke="#4d4d4f"/></svg>+ (07) 3250 6190</li>
    <li><svg viewBox="0 0 14 12"><rect x="0.5" y="1.5" width="13" height="9" fill="#4d4d4f"/><polyline points="0.5,1.5 7,7 13.5,1.5" fill="none" stroke="#fff" stroke-width="1"/></svg>projects.klestates@gmail.com</li>
    <li><svg viewBox="0 0 14 12"><path d="M1 5 Q1 1 5 1 H13 V9 H1 Z" fill="#4d4d4f"/><rect x="6" y="9" width="2" height="3" fill="#4d4d4f"/><rect x="8" y="3" width="3" height="2" fill="#fff"/></svg>PO Box 2214 Eastwood North QLD 4120</li>
  </ul>
  <div class="footer-band"><svg width="44" height="25" viewBox="0 0 44 25"><polygon points="0,1 9,1 20,12.5 9,24 0,24 11,12.5" fill="#fff"/><polygon points="18,1 27,1 38,12.5 27,24 18,24 29,12.5" fill="#fff"/></svg></div>
  <div class="footer-stripe"></div>
</section>

<section class="card card--back row-1" role="img" aria-label="Blue brushed texture background">
  <div class="wordmark"><span class="wordmark__dot"></span><span class="wordmark__name">KL ESTATES</span></div>
</section>

<section class="card card--front row-2">
  <div class="wordmark"><span class="wordmark__dot"></span><span class="wordmark__name">KL ESTATES</span></div>
  <div class="person">
    <p class="person__name">DANIEL HART</p>
    <svg class="person__bar" width="220" height="11" viewBox="0 0 220 11"><polygon points="0,2 88,2 92,5.5 88,9 0,9" fill="#464749"/><polygon points="92,0 212,0 218,5.5 212,11 92,11 97,5.5" fill="#464749"/></svg>
    <p class="person__role">GENERAL MANAGER</p>
  </div>
  <div class="divider"></div>
  <ul class="contacts">
    <li><svg viewBox="0 0 14 12"><rect x="1" y="1" width="12" height="7" fill="none" stroke="#4d4d4f" stroke-width="1.5"/><rect x="0" y="9" width="14" height="2.5" fill="#4d4d4f"/></svg>+ (07) 3250 6184</li>
    <li><svg viewBox="0 0 14 12"><rect x="3" y="0" width="8" height="4" fill="#4d4d4f"/><rect x="0" y="4" width="14" height="5" rx="1" fill="#4d4d4f"/><rect x="3" y="8" width="8" height="4" fill="#fff" stroke="#4d4d4f"/></svg>+ (07) 3250 6190</li>
    <li><svg viewBox="0 0 14 12"><rect x="0.5" y="1.5" width="13" height="9" fill="#4d4d4f"/><polyline points="0.5,1.5 7,7 13.5,1.5" fill="none" stroke="#fff" stroke-width="1"/></svg>projects.klestates@gmail.com</li>
    <li><svg viewBox="0 0 14 12"><path d="M1 5 Q1 1 5 1 H13 V9 H1 Z" fill="#4d4d4f"/><rect x="6" y="9" width="2" height="3" fill="#4d4d4f"/><rect x="8" y="3" width="3" height="2" fill="#fff"/></svg>PO Box 2214 Eastwood North QLD 4120</li>
  </ul>
  <div class="footer-band"><svg width="44" height="25" viewBox="0 0 44 25"><polygon points="0,1 9,1 20,12.5 9,24 0,24 11,12.5" fill="#fff"/><polygon points="18,1 27,1 38,12.5 27,24 18,24 29,12.5" fill="#fff"/></svg></div>
  <div class="footer-stripe"></div>
</section>

<section class="card card--back row-2" role="img" aria-label="Blue brushed texture background with a large faint brand shape">
  <div class="back-ring"></div>
  <div class="wordmark"><span class="wordmark__dot"></span><span class="wordmark__name">KL ESTATES</span></div>
</section>

</body>
</html>
```